Halvern Partners M&A Email Newsletter Design

Halvern Partners is a Marketing/Consulting/M&A company and we want to find a graphic designer experienced in newsletter design. Please visit our website for more information and to see our logo. We would like the color scheme of the newsletter to reflect our colors of blue, yellow, and dark gray (see website for visual representation). The newsletter will focus on detailing M&A news in the market. Please reach out if you have any questions. https://www.halvernpartners-example.net/

Marketing

Font styles to use
Serif
Sans Serif

Colors
0456a4
ffc214
ffcf3e

Requirements
Must have
• Halvern Partners' Color Scheme: Yellow, Blue, Dark Gray (see website)
Professional economics newsletter
Should not have
• Strange/hard to read fonts

```html
<!DOCTYPE html>
<html lang="en">
<head>
<meta charset="utf-8">
<title>Halvern Partners – M&amp;A Transaction Newsletter</title>
<link rel="stylesheet" href="https://fonts.googleapis.com/css2?family=Roboto:wght@100;300;400;500;700;900&display=swap">
<style>
:root{
  --blue:#2a4fa8;
  --brand-blue:#0456a4;
  --yellow:#ffc214;
  --yellow-light:#ffcf3e;
  --yellow-deep:#e9a90c;
  --dark:#262626;
  --ink:#1a1a1a;
  --body:#555;
  --muted:#8a8a8a;
  --panel:#f1f1f1;
  --card:#efefef;
  --rule:#d6d6d6;
  --stage:#e6e6e6;
}
*{margin:0;padding:0;box-sizing:border-box}
html,body{width:1200px;height:686px;overflow:hidden;background:var(--stage);font-family:"Roboto",Arial,sans-serif;color:var(--ink)}
.canvas{position:relative;width:1200px;height:686px}
.page{position:absolute;top:37px;width:471px;height:611px;background:#fff;overflow:hidden}
.page--front{left:103px}
.page--inside{left:625px}
.abs{position:absolute}
.deco{position:absolute;left:0;top:0;width:471px;height:611px}
.top-bar{position:absolute;left:258px;top:0;width:213px;height:13px;background:var(--blue)}

/* front header */
.masthead{position:absolute;left:0;top:26px;width:382px;height:83px;background:var(--panel)}
.masthead__title{position:absolute;left:38px;top:14px;font-weight:100;font-size:38px;letter-spacing:-0.5px;line-height:1;color:var(--ink)}
.masthead__meta{position:absolute;left:40px;top:57px;display:flex;align-items:center;font-size:8.4px;font-weight:500;color:var(--ink)}
.masthead__meta span{padding:0 15px}
.masthead__meta span:first-child{padding-left:0}
.masthead__meta i{display:block;width:1px;height:12px;background:#999}
.brand{position:absolute;left:318px;top:58px;display:flex;align-items:center;gap:5px}
.brand__name{font-size:13.5px;font-weight:500;color:var(--yellow-deep);letter-spacing:-0.2px}
.brand__dot{width:7px;height:7px;background:var(--yellow)}

.mission{position:absolute;left:41px;top:121px;width:175px;font-size:16.4px;line-height:19.4px;font-weight:700;color:var(--yellow-deep)}
.mission-rule{position:absolute;left:41px;top:304px;width:170px;height:2px;background:var(--blue)}
.section-title{position:absolute;left:41px;top:314px;font-size:15px;font-weight:700;color:var(--ink);letter-spacing:-0.1px}
.services{position:absolute;left:0;top:341px;width:211px}
.service{padding:0 0 7px 41px;border-bottom:1px solid var(--rule);margin-bottom:7px}
.service:last-child{border:none}
.service h3{font-size:7.6px;font-weight:700;text-transform:uppercase;margin-bottom:1px}
.service p{font-size:7.4px;line-height:10.8px;font-weight:300;color:var(--body)}

.photo{position:absolute}
.photo--compass{left:258px;top:122px;width:172px;height:114px;background:radial-gradient(circle at 40% 70%,#e9ecef 0%,#c9cdd3 55%,#8f969f 100%)}
.feature-list{position:absolute;left:258px;top:252px;width:173px}
.feature{position:absolute;left:0;width:173px;height:72px;background:var(--card)}
.feature__thumb{position:absolute;left:8px;top:7px;width:45px;height:51px}
.feature__text{position:absolute;left:61px;top:6px;width:108px}
.feature__title{font-size:6.9px;line-height:8.4px;font-weight:500;color:var(--ink)}
.feature__summary{font-size:6.7px;line-height:8.2px;font-weight:300;color:var(--body)}
.feature__meta{position:absolute;left:61px;bottom:5px;font-size:5.4px;font-weight:500;color:var(--muted);display:flex;gap:12px}

.page-num{position:absolute;left:449px;top:563px;width:16px;height:20px}
.footer{position:absolute;left:0;top:589px;width:471px;height:22px;background:var(--dark)}
.footer__url{position:absolute;right:226px;top:0;line-height:22px;font-size:7.6px;letter-spacing:1.8px;color:#fff;font-weight:400}
.footer__issue{position:absolute;left:258px;top:0;width:173px;height:22px;background:var(--blue);color:#fff;font-size:5.6px;line-height:22px;padding-left:11px}

/* inside page */
.article__title{position:absolute;left:42px;top:71px;width:200px;font-size:15.2px;line-height:18.6px;font-weight:700;text-transform:uppercase;color:var(--ink)}
.article__date{position:absolute;left:42px;top:150px;font-size:6px;font-weight:500;color:var(--muted)}
.photo--start{left:259px;top:42px;width:171px;height:114px;background:linear-gradient(180deg,#3a3a3a 0%,#6e6e6e 55%,#8a2a2a 76%,#b3272a 86%,#7a7a7a 100%)}
.col{position:absolute;font-size:7.3px;line-height:10.8px;font-weight:300;color:var(--body);text-align:justify;overflow:hidden}
.col p{margin-bottom:6px}
.col strong{display:block;font-weight:500;color:var(--ink);margin-bottom:6px;text-align:left}
.col--one{left:42px;top:174px;width:194px;height:395px}
.col--two{left:259px;top:180px;width:171px;height:395px}
.col .lead{text-transform:uppercase;font-weight:700;color:var(--ink)}
.col .wrap-short{width:92px;text-align:left}
</style>
</head>
<body>
<div class="canvas">

  <!-- Front page -->
  <section class="page page--front">
    <svg class="deco" viewBox="0 0 471 611" aria-hidden="true">
      <polygon points="382,109 471,109 471,462 395,390 430,340 430,109" fill="var(--yellow)"/>
      <polygon points="300,330 471,330 471,462" fill="var(--yellow-light)"/>
      <polygon points="224,257 258,229 258,285" fill="var(--yellow)"/>
      <polygon points="0,516 64,568 0,589" fill="var(--yellow)"/>
      <polygon points="0,540 34,568 0,589" fill="var(--yellow-deep)"/>
      <polygon points="0,311 16,324 0,337" fill="var(--blue)"/>
    </svg>
    <div class="top-bar"></div>

    <header class="masthead">
      <h1 class="masthead__title">NEWSLETTER</h1>
      <div class="masthead__meta"><span>Issue Number</span><i></i><span>Jan-July, 2020</span><i></i><span>Volume 1</span></div>
    </header>
    <div class="brand"><span class="brand__name">Halvern Partners</span><span class="brand__dot"></span></div>

    <p class="mission">Halvern Partners exists to help the owners of independent marketing communications agencies achieve their ambitions and maximize the value of their life's work.</p>
    <div class="mission-rule"></div>
    <h2 class="section-title">M&amp;A TRANSACTIONS</h2>

    <div class="services">
      <div class="service">
        <h3>Sales Readiness Assessment</h3>
        <p>Make sure your agency is firing on all cylinders at the time of sale to maximize your current value and any potential earnout.</p>
      </div>
      <div class="service">
        <h3>Four-Phase External Sale Process</h3>
        <p>- Readiness assessment<br>- Valuation<br>- Suitor identification<br>- Transaction evaluation and negotiation</p>
      </div>
      <div class="service">
        <h3>Internal Sale</h3>
        <p>Designed to transfer ownership to your designated successor over time, on your terms and where you stay in control throughout.</p>
      </div>
      <div class="service">
        <h3>Employee Stock Ownership Plans</h3>
      </div>
    </div>

    <div class="photo photo--compass" role="img" aria-label="Photo of a compass dial with the word success around its rim"></div>

    <div class="feature-list">
      <article class="feature" style="top:0">
        <div class="feature__thumb" role="img" aria-label="Photo of dress shoes standing behind a red start here line" style="background:linear-gradient(180deg,#2e2e2e 0%,#777 60%,#b3272a 72%,#9a9a9a 100%)"></div>
        <div class="feature__text">
          <p class="feature__title">Agency owners - When the M&amp;A market rebounds, will you be ready?</p>
          <p class="feature__summary">For M&amp;A tomorrow, establish your strategy and prepare today. M&amp;A will rebound. Be ready.</p>
        </div>
        <div class="feature__meta"><span>Read more on page 1</span><span>MAY 7, 2020</span></div>
      </article>
      <article class="feature" style="top:87px">
        <div class="feature__thumb" role="img" aria-label="Photo of a hand pulling a block from a wooden block tower" style="background:linear-gradient(135deg,#f2ede6 0%,#c9925a 55%,#e8e2da 100%)"></div>
        <div class="feature__text">
          <p class="feature__title">What agency owners need to know about buying another agency</p>
          <p class="feature__summary">Buying an agency requires managing risk. Thinking of buying an agency? Here are some important considerations.</p>
        </div>
        <div class="feature__meta"><span>Read more on page 2</span><span>MAR 12, 2020</span></div>
      </article>
      <article class="feature" style="top:175px">
        <div class="feature__thumb" role="img" aria-label="Photo of a walking businessman carrying a leather bag" style="background:linear-gradient(135deg,#f4f6f8 0%,#3d5a86 50%,#8a5a36 75%,#eef0f2 100%)"></div>
        <div class="feature__text">
          <p class="feature__title">Vital strategies you must consider before selling your digital agency</p>
          <p class="feature__summary">Halvern Partners' digital practice leader Neil Ardmore guides you through all the essential steps of selling your agency.</p>
        </div>
        <div class="feature__meta"><span>Read more on page 3</span><span>NOV 21, 2019</span></div>
      </article>
      <article class="feature" style="top:268px;height:65px">
        <div class="feature__thumb" role="img" aria-label="Photo of a golden egg resting in a nest" style="background:radial-gradient(circle at 50% 40%,#e6c77a 0%,#a8843e 45%,#f1ede4 100%)"></div>
        <div class="feature__text">
          <p class="feature__title">What is your agency worth? And why it's important to know</p>
          <p class="feature__summary">One day, you'll want all your life's work to pay off.</p>
        </div>
        <div class="feature__meta"><span>Read more on page 4</span><span>NOV 21, 2019</span></div>
      </article>
    </div>

    <svg class="page-num" viewBox="0 0 16 20" aria-label="Page 1"><polygon points="0,0 16,10 0,20" fill="var(--blue)"/><text x="4" y="13" font-size="6" fill="#fff" font-family="Roboto, sans-serif">1</text></svg>

    <footer class="footer">
      <span class="footer__url">www.halvernpartners-example.net</span>
      <span class="footer__issue">M&amp;A TRANSACTION NEWSLETTER, JAN-JULY, 2020, VOL-1</span>
    </footer>
  </section>

  <!-- Inside page -->
  <section class="page page--inside">
    <svg class="deco" viewBox="0 0 471 611" aria-hidden="true">
      <polygon points="0,0 86,0 42,53" fill="var(--yellow)"/>
      <polygon points="0,0 30,0 42,53" fill="var(--yellow-deep)"/>
      <polygon points="430,45 471,13 471,288 326,156 430,156" fill="var(--yellow)"/>
      <polygon points="400,156 471,225 471,288 360,185" fill="var(--yellow-deep)"/>
      <polygon points="0,65 16,78 0,92" fill="var(--blue)"/>
    </svg>
    <div class="top-bar"></div>

    <h1 class="article__title">Agency owners - when the M&amp;A market rebounds, will you be ready?</h1>
    <p class="article__date">MAY 7, 2020</p>

    <div class="photo photo--start" role="img" aria-label="Photo of dress shoes on asphalt behind a red start here line"></div>

    <div class="col col--one">
      <strong class="lead">For M&amp;A tomorrow, establish your strategy and prepare today.</strong>
      <strong>M&amp;A will rebound. Be ready.</strong>
      <p>While M&amp;A activity for communications firms has diminished dramatically if not shut down completely, now is the time to reassess your M&amp;A strategy. Whether buyer or seller, you should ensure that you're best prepared to act when the market rebounds.</p>
      <strong>Strategic considerations for buyers.</strong>
      <p>Your acquisition strategy must align with the long-term needs of your agency and guide against pursuing ill-fitting firms that would divert valuable resources and strain the overall business.</p>
      <p>You should review this strategy periodically, adjusting to changes in the business and industry so that you remain on the right course. Also, new opportunities may present themselves that compel you to rethink the current criteria and adjust if needed.</p>
      <p>Any significant changes to your M&amp;A strategy should result from a thoughtful process. Whatever your established strategy may be, the acquisition team should fully understand it and agree across the board.</p>
      <p>We propose the following six considerations for developing a disciplined and strategic pursuit of acquisition targets:</p>
      <p>What is the desired range of services involved? Are you looking to enhance existing capabilities or invest in new, complementary services? Have you assessed the market to understand its direction and competitor activity?</p>
      <p>What are the preferred industry sectors? Do you want to serve new industry categories?</p>
      <p>What are the preferred and minimum revenue levels? Obviously, this targeting depends upon the level of capital available. However, you should stay within a compatible revenue range for your firm</p>
    </div>

    <div class="col col--two">
      <p class="wrap-short">as well as pursue candidate businesses with a history of growth.</p>
      <strong>Strategic considerations for sellers.</strong>
      <p>If you're thinking of selling your agency, now is a good time to make sure that you understand a buyer's perception of risk. Make frank assessments to identify and address any shortcomings in your firm. Map out the ideal characteristics of the right buyer for your agency and culture. These preparations will help you develop a well-formed strategy to ensure the highest valuation and future potential for your business.</p>
      <p>Consider the following nine areas to gauge your readiness... and recondition your firm as necessary:</p>
      <p>Do you have the right leadership team and depth of management or does your firm overly rely on its ownership (you) for success? A team incapable of sustaining growth diminishes the value and thus attractiveness of your agency. Now could be a good time to look for bona fide talent newly on the market due to numerous staff reductions nationwide.</p>
      <p>Do you understand what your business valuation might be, assuming a normal market? It's always good for you to understand your firm's value, as well as the current M&amp;A climate, so that you align your expectations with reality and avoid failure in attempting to sell. Valuation of your agency will enable you to know quite quickly if a sales process with a particular buyer is worth pursuing. Be ready to walk away from a transaction value that's beneath your expectations. Knowing your firm's worth will help you remain disciplined.</p>
    </div>

    <svg class="page-num" style="left:447px" viewBox="0 0 16 20" aria-label="Page 2"><polygon points="0,0 16,10 0,20" fill="var(--blue)"/><text x="4" y="13" font-size="6" fill="#fff" font-family="Roboto, sans-serif">2</text></svg>

    <footer class="footer">
      <span class="footer__url">www.halvernpartners-example.net</span>
      <span class="footer__issue">M&amp;A TRANSACTION NEWSLETTER, JAN-JULY, 2020, VOL-1</span>
    </footer>
  </section>

</div>
</body>
</html>
```